Brightpath, LLC
Electrical Contracting Company
We really like the back of #125 & #126 and the logo design on the front of #125.
We liked the front layout of #122, and we especially liked how they included the phrase Electrical Contracting Company on the card.
#118 we really like the front and back of your card. We like the colors, we like the shadowing.
We like the symbols for phone, cell, etc.
The above info was updated in the brief summary.
Please not changes to information:
instead of Electrical Contracting Corporation it needs to be Electrical Contracting Company
And the Fax number is 612-437-2908

```html
<!DOCTYPE html>
<html lang="en">
<head>
<meta charset="utf-8">
<title>Brightpath, LLC – Business Cards</title>
<link href="https://fonts.googleapis.com/css2?family=Arimo:wght@400;700&display=swap" rel="stylesheet">
<style>
  :root {
    --stage: #e9eaeb;
    --stage-edge: #c9cacc;
    --card-black: #0d0d0d;
    --card-black-soft: #2a2a2a;
    --card-white: #ffffff;
    --gold: #d9b24a;
    --gold-deep: #9c7a26;
    --ink: #1a1a1a;
    --ink-soft: #555555;
  }
  * { margin: 0; padding: 0; box-sizing: border-box; }
  html, body { width: 1200px; height: 947px; overflow: hidden; }
  body {
    font-family: "Arimo", Arial, sans-serif;
    background: radial-gradient(ellipse at 45% 40%, #f7f7f7 0%, var(--stage) 55%, var(--stage-edge) 100%);
    position: relative;
  }

  /* Brand block, top right */
  .brand-block {
    position: absolute; top: 40px; right: 60px; width: 240px;
    display: flex; flex-direction: column; align-items: center; gap: 8px;
  }
  .brand-block .mark-dot {
    width: 64px; height: 64px; border-radius: 50%; border: 4px solid var(--ink);
  }
  .brand-block .brand-name { font-weight: 700; font-size: 26px; color: var(--ink); }
  .brand-block .brand-tag { font-size: 12px; color: var(--ink); }

  .card {
    position: absolute; border-radius: 16px; overflow: hidden;
    box-shadow: 0 18px 30px rgba(0,0,0,.35), 0 3px 6px rgba(0,0,0,.25);
  }

  /* Back of card */
  .card-back {
    left: 90px; top: 90px; width: 560px; height: 320px;
    background: linear-gradient(160deg, var(--card-black-soft) 0%, var(--card-black) 60%);
    display: flex; align-items: center; justify-content: center; gap: 16px;
  }
  .card-back .mark-dot {
    width: 58px; height: 58px; border-radius: 50%;
    border: 5px solid var(--gold); background: var(--card-black);
  }
  .card-back .brand-name { color: var(--gold); font-weight: 700; font-size: 24px; }

  /* Front of card */
  .card-front {
    left: 380px; top: 430px; width: 660px; height: 377px;
    display: flex; background: var(--card-white);
  }
  .card-front .brand-panel {
    width: 300px; height: 100%; position: relative;
    background: linear-gradient(160deg, var(--card-black-soft) 0%, var(--card-black) 65%);
    display: flex; flex-direction: column; align-items: center; justify-content: center; gap: 10px;
    padding-right: 40px;
  }
  .brand-panel .mark-dot {
    width: 96px; height: 96px; border-radius: 50%;
    border: 7px solid var(--gold); background: var(--card-black);
  }
  .brand-panel .brand-name { color: var(--gold); font-weight: 700; font-size: 24px; }
  .brand-panel .brand-tag { color: var(--gold); font-size: 12px; margin-top: -6px; }
  .brand-panel .web {
    position: absolute; right: 14px; top: 50%;
    transform: translateY(-50%) rotate(90deg); transform-origin: center;
    color: #fff; font-weight: 700; font-size: 15px; white-space: nowrap;
    width: 20px; display: flex; justify-content: center;
  }

  .contact-panel { flex: 1; padding: 40px 30px 30px 36px; color: var(--ink); }
  .contact-panel .person { font-weight: 700; font-size: 26px; }
  .contact-panel .role { font-size: 14px; color: var(--ink-soft); margin-top: 3px; }
  .contact-panel .address { margin-top: 38px; font-size: 15px; line-height: 1.3; display: flex; gap: 6px; }
  .contact-panel .lines { margin-top: 18px; font-size: 15px; line-height: 1.35; }
  .contact-panel .lines dt { font-weight: 700; float: left; width: 52px; clear: left; }
  .contact-panel .lines dd { margin-left: 52px; }
  .contact-panel .email { margin-top: 30px; font-size: 15px; }
</style>
</head>
<body>

  <section class="brand-block" aria-label="Brightpath brand">
    <span class="mark-dot"></span>
    <span class="brand-name">Brightpath, LLC</span>
    <span class="brand-tag">Electrical Contracting Company</span>
  </section>

  <article class="card card-back" aria-label="Card back">
    <span class="mark-dot"></span>
    <span class="brand-name">Brightpath, LLC</span>
  </article>

  <article class="card card-front" aria-label="Card front">
    <div class="brand-panel">
      <span class="mark-dot"></span>
      <span class="brand-name">Brightpath, LLC</span>
      <span class="brand-tag">Electrical Contracting Company</span>
      <span class="web">www.brightpathllc.com</span>
    </div>
    <div class="contact-panel">
      <div class="person">Dana Holt</div>
      <div class="role">President</div>
      <div class="address">
        <span>Address</span>
        <span>48 Ridge Hollow Rd.<br>Lakemont, NY 14857</span>
      </div>
      <dl class="lines">
        <dt>Phone</dt><dd>6124371154</dd>
        <dt>Cell</dt><dd>6124376620</dd>
        <dt>Fax</dt><dd>6124372908</dd>
      </dl>
      <div class="email">dana@brightpathllc.com</div>
    </div>
  </article>

</body>
</html>
```